Multi-purose Thank You Card Design Project (Real Estate)

We are in the business of listing and selling luxury homes in Atlanta Georgia and are the #1 Award Winning team in our office, #5 in Georgia and #5 in Southeast for all Brennan Oakes team. Your can learn more about us at www.marlowandpartners.example.

In our business model, growing a team to $80 million in sales (we will sell $40,000,000 in 2013 and are determined to grow rapidly while providing high levels of service) requires that we carefully nurture our sphere of influence database through multiple, high quality, well-designed touches like (thank you cards, letters, phone calls, gifts etc)

We need a thank you card:
1. Can be used for multiple purposes
a. Referral thank you.
b. House closing anniversary thank you
2. File built in Photoshop with layers that we can edit (we are proficient in Photoshop)
3. Design based on the Brennan Oakes luxury Style Guide but does not restrict your creativity. Break the rules and have more impact.
5. Card 7" w x 5' h opening at top
Updates

The attached logo files have been replaced and should open correctly.
Kindly,
Garrick

Target Market(s)

Buyers and Seller of Homes from $300k to $10m

Industry/Entity Type

Business

Requirements
Must have
• Copy on cover: "Thanks for the Referral"
Logo 1: Brennan Oakes Luxury Logo
File in 300 dpi for print
File in 96 dpi for use with Post Ahead Notes
Nice to have
• Photo of Home (optional)
Logo 2 Marlow and Partners Logo (optional)

```html
<!DOCTYPE html>
<html lang="en">
<head>
<meta charset="utf-8">
<title>Referral Thank You Card</title>
<link rel="stylesheet" href="https://fonts.googleapis.com/css2?family=Oswald:wght@500;700&family=Great+Vibes&family=Handlee&family=Federo&family=Montserrat:wght@400&display=swap">
<style>
  :root {
    --card-dark: #2a2a2a;
    --badge-grey: #5f5f5f;
    --crimson: #d32a4a;
    --paper-top: #e8e8e8;
    --paper-bottom: #dcdcdc;
    --ink: #1f1f1f;
    --white: #ffffff;
    --fold: #8a8a8a;
  }
  * { margin: 0; padding: 0; box-sizing: border-box; }
  html, body { width: 1200px; height: 839px; overflow: hidden; background: var(--white); }
  .canvas { position: relative; width: 1200px; height: 839px; }

  /* Outside of card */
  .card-outside { position: absolute; left: 0; top: 0; width: 587px; height: 839px; background: var(--card-dark); }
  .card-outside svg { position: absolute; inset: 0; }
  .ornament {
    position: absolute;
    background: radial-gradient(ellipse at center, rgba(211,42,74,.55) 0%, rgba(211,42,74,.25) 55%, rgba(211,42,74,0) 75%);
  }

  /* Back logo block, printed upside down so it reads when the card stands */
  .back-logo { position: absolute; transform: rotate(180deg); color: var(--white); font-family: "Montserrat", sans-serif; font-weight: 400; text-transform: uppercase; white-space: nowrap; }
  .back-logo.company { left: 170px; top: 24px; width: 248px; height: 16px; font-size: 10px; letter-spacing: 3px; line-height: 16px; text-align: center; }
  .back-logo.division { left: 172px; top: 54px; width: 160px; height: 42px; text-align: center; }
  .back-logo.division .name { display: block; font-size: 17px; letter-spacing: 2px; line-height: 22px; }
  .back-logo.division .sub { display: block; font-size: 9.5px; letter-spacing: 3.5px; line-height: 16px; }
  .back-logo-mark { position: absolute; left: 352px; top: 62px; width: 16px; height: 16px; background: var(--crimson); }

  .cover-title { position: absolute; left: 172px; top: 560px; width: 240px; height: 150px; }
  .cover-title .thank { position: absolute; left: 36px; top: 16px; font-family: "Great Vibes", cursive; font-size: 60px; color: var(--crimson); line-height: 1; }
  .cover-title .referral { position: absolute; left: 113px; top: 20px; font-family: "Oswald", sans-serif; font-weight: 700; font-size: 19px; color: var(--white); line-height: 1; }
  .cover-title .you { position: absolute; left: 76px; top: 66px; font-family: "Oswald", sans-serif; font-weight: 700; font-size: 53px; color: var(--white); line-height: 1; }

  /* Inside of card */
  .card-inside { position: absolute; left: 612px; top: 0; width: 588px; height: 839px; }
  .inside-top { position: absolute; left: 0; top: 0; width: 588px; height: 420px; background: var(--paper-top); }
  .inside-bottom { position: absolute; left: 0; top: 420px; width: 588px; height: 419px; background: var(--paper-bottom); }
  .tile { position: absolute; }
  .tile.accent { background: var(--crimson); }
  .photo-exterior { background: linear-gradient(180deg, #2f5fb0 0%, #8aa6cf 45%, #e9e6de 60%, #4c7a2e 100%); }
  .photo-stair { background: linear-gradient(160deg, #a27a4a 0%, #6b4a2c 50%, #d4b486 100%); }
  .photo-terrace { background: linear-gradient(180deg, #d6ccc0 0%, #c4bfb6 60%, #d9d4cc 100%); }
  .photo-stone-day { background: linear-gradient(180deg, #cbc9c6 0%, #b6aa98 60%, #c6c2b6 100%); }
  .photo-stone-night { background: linear-gradient(180deg, #1d2a3a 0%, #6b5338 55%, #3f4a2a 100%); }
  .photo-living-pale { background: linear-gradient(180deg, #e6dccb 0%, #d8c8ac 60%, #cfc2b0 100%); }
  .photo-living { background: linear-gradient(180deg, #d9b77e 0%, #b48a52 55%, #5a4431 100%); }

  .band { position: absolute; left: 164px; width: 260px; background: var(--crimson); }
  .message {
    position: absolute; left: 174px; top: 474px; width: 242px;
    font-family: "Handlee", cursive; font-size: 12.6px; line-height: 22.7px;
    letter-spacing: .7px; word-spacing: 1px;
    color: var(--ink); text-align: justify;
  }
  .message p + p { margin-top: 9px; }
  .sign-off { position: absolute; left: 174px; top: 746px; font-family: "Federo", serif; font-size: 38px; color: var(--ink); line-height: 1; }
</style>
</head>
<body>
<div class="canvas">

  <section class="card-outside">
    <svg width="587" height="839" viewBox="0 0 587 839" aria-hidden="true">
      <line x1="20" y1="18" x2="162" y2="18" stroke="#d32a4a" stroke-width="1.5"/>
      <line x1="20" y1="18" x2="20" y2="150" stroke="#d32a4a" stroke-width="1.5"/>
      <line x1="425" y1="18" x2="568" y2="18" stroke="#d32a4a" stroke-width="1.5"/>
      <line x1="568" y1="18" x2="568" y2="150" stroke="#d32a4a" stroke-width="1.5"/>
      <line x1="170" y1="47" x2="418" y2="47" stroke="#ffffff" stroke-width="1"/>
      <line x1="337" y1="47" x2="337" y2="100" stroke="#ffffff" stroke-width="1"/>
      <line x1="0" y1="419.5" x2="587" y2="419.5" stroke="#8a8a8a" stroke-width="1"/>
      <path d="M172,582 L212,548 Q292,528 372,548 L412,582 L412,682 L372,712 Q292,732 212,712 L172,682 Z" fill="#5f5f5f"/>
      <line x1="208" y1="538" x2="132" y2="626" stroke="#d32a4a" stroke-width="1.5"/>
      <line x1="132" y1="636" x2="208" y2="722" stroke="#d32a4a" stroke-width="1.5"/>
      <line x1="378" y1="538" x2="454" y2="626" stroke="#d32a4a" stroke-width="1.5"/>
      <line x1="454" y1="636" x2="378" y2="722" stroke="#d32a4a" stroke-width="1.5"/>
    </svg>
    <div class="ornament" style="left:22px;top:20px;width:40px;height:56px;" role="img" aria-label="Crimson scroll flourish in top left corner"></div>
    <div class="ornament" style="left:526px;top:20px;width:40px;height:56px;" role="img" aria-label="Crimson scroll flourish in top right corner"></div>
    <div class="ornament" style="left:118px;top:600px;width:52px;height:64px;" role="img" aria-label="Crimson scroll flourish left of the title badge"></div>
    <div class="ornament" style="left:416px;top:600px;width:52px;height:64px;" role="img" aria-label="Crimson scroll flourish right of the title badge"></div>

    <div class="back-logo company">Brennan Oakes Estates</div>
    <div class="back-logo division"><span class="name">Luxury Homes</span><span class="sub">Collection</span></div>
    <div class="back-logo-mark"></div>

    <div class="cover-title">
      <span class="thank">Thank</span>
      <span class="referral">referral</span>
      <span class="you">YOU...</span>
    </div>
  </section>

  <section class="card-inside">
    <div class="inside-top">
      <div class="tile photo-exterior" style="left:0;top:80px;width:156px;height:95px;" role="img" aria-label="White luxury villa with palm trees at dusk"></div>
      <div class="tile photo-stair" style="left:165px;top:0;width:119px;height:175px;" role="img" aria-label="Curved staircase with wrought iron railing and chandelier"></div>
      <div class="tile photo-terrace" style="left:293px;top:80px;width:139px;height:95px;" role="img" aria-label="Faded view of a glass-walled terrace"></div>
      <div class="tile accent" style="left:441px;top:80px;width:147px;height:95px;"></div>
      <div class="tile photo-stone-day" style="left:165px;top:184px;width:129px;height:105px;" role="img" aria-label="Faded stone house exterior"></div>
      <div class="tile photo-stone-night" style="left:299px;top:184px;width:134px;height:105px;" role="img" aria-label="Stone house lit at night"></div>
      <div class="tile accent" style="left:0;top:297px;width:272px;height:95px;"></div>
      <div class="tile photo-living-pale" style="left:281px;top:297px;width:152px;height:95px;" role="img" aria-label="Faded living room with arched windows and fireplace"></div>
      <div class="tile photo-living" style="left:442px;top:297px;width:146px;height:95px;" role="img" aria-label="Living room with arched windows and stone fireplace"></div>
    </div>
    <div class="inside-bottom"></div>
    <div class="band" style="top:420px;height:18px;"></div>
    <div class="message">
      <p>Lorem ipsum dolor sit amet, consectetuer adipiscing elit. Nam cursus. Morbi ut mi. Nullam enim leo, egestas id, condimentum at, laoreet mattis, massa.</p>
      <p>Sed eleifend nonummy diam. Praesent mauris ante, elementum et, bibendum at, posuere sit amet, nibh. Duis tincidunt lectus quis dui viverra vestibulum.</p>
      <p>Maecenas placerat, nisl at consequat rhoncus, sem nunc gravida justo, quis eleifend arcu velit quis lacus.</p>
    </div>
    <div class="sign-off">Thank You...!</div>
    <div class="band" style="top:820px;height:19px;"></div>
  </section>

</div>
</body>
</html>
```